Consulting/Brand Licensing business needs business card

We need a business card created for our IP company, that also does consulting and brand licensing. We would like this card to be vague, as our other business' are in the cannabis industry and this is a non-cannabis touching entity. Perhaps something that hints vaguely at the industry without alerting or possibly offending the receiver.

Target Market(s)

CEOs/Key Decision Makers/Industry Leaders

Contact Information for Business Card

No address, simply list Seattle, WA. Phone: 206-555-0147. Name: Dilan Vesterby // email: Dilan@pulvanixa.com

Colors

Designer to choose colors to be used in the design.

Requirements
Must have
• Logo, Name, Email, Phone number, "Consulting, Licensing and Branding Specialists"
Nice to have
• We would like this to be more professional than playful.

```html
<!DOCTYPE html>
<html lang="en">
<head>
<meta charset="utf-8">
<title>Pulvanixa, Inc — Business Card</title>
<link href="https://fonts.googleapis.com/css2?family=Open+Sans:wght@400;700;800&display=swap" rel="stylesheet">
<style>
  :root {
    --orange-deep: #c63e1e;
    --orange: #dc5531;
    --orange-light: #e8704c;
    --orange-faint: #fbe9e3;
    --paper: #ffffff;
    --ink: #3a3a3a;
    --rule: #8a8a8a;
    --backdrop: #e6e6e6;
  }
  * { margin: 0; padding: 0; box-sizing: border-box; }
  html, body {
    width: 1200px; height: 900px; overflow: hidden;
    background: var(--backdrop);
    font-family: "Open Sans", Arial, sans-serif;
  }
  .sheet {
    width: 1200px; height: 900px;
    display: flex; flex-direction: column;
    align-items: center; justify-content: center; gap: 24px;
  }
  .card {
    position: relative; width: 700px; height: 400px; overflow: hidden;
    box-shadow: 0 6px 18px rgba(0,0,0,0.18);
  }
  .card-front {
    background: linear-gradient(135deg, var(--orange-deep) 0%, var(--orange) 50%, var(--orange-light) 100%);
    display: flex; align-items: center; justify-content: center;
  }
  .front-wordmark {
    color: var(--paper); font-weight: 800; font-size: 64px; letter-spacing: 2px;
  }
  .card-back { background: var(--paper); }
  .backdrop-wordmark {
    position: absolute; top: 22px; right: 40px;
    font-weight: 800; font-size: 96px; color: var(--orange-faint);
    letter-spacing: 2px; white-space: nowrap; line-height: 1;
  }
  .brand {
    position: absolute; left: 48px; top: 160px;
  }
  .brand-row { display: flex; align-items: center; gap: 14px; }
  .brand-mark { width: 22px; height: 22px; background: var(--orange); }
  .brand-name { color: var(--orange); font-weight: 800; font-size: 40px; letter-spacing: 0.5px; line-height: 1.1; }
  .tagline {
    margin-top: 6px; margin-left: 36px;
    color: var(--ink); font-weight: 400; font-size: 15px; letter-spacing: 0.3px;
  }
  .contact-block {
    position: absolute; right: 48px; bottom: 48px;
    display: flex; align-items: center; gap: 18px;
  }
  .person-name {
    color: var(--orange); font-weight: 700; font-size: 22px; letter-spacing: 0.5px;
    text-transform: uppercase; align-self: flex-end;
  }
  .divider { width: 1px; height: 78px; background: var(--rule); }
  .contact-list { list-style: none; color: var(--ink); font-size: 17px; line-height: 26px; }
  .contact-list li { display: flex; align-items: center; gap: 8px; }
  .contact-list svg { width: 14px; height: 14px; fill: var(--orange); flex: none; }
</style>
</head>
<body>
<main class="sheet">
  <section class="card card-front" aria-label="Card front">
    <span class="front-wordmark">Pulvanixa</span>
  </section>

  <section class="card card-back" aria-label="Card back">
    <span class="backdrop-wordmark" aria-hidden="true">Pulvanixa</span>
    <div class="brand">
      <div class="brand-row">
        <span class="brand-mark"></span>
        <span class="brand-name">Pulvanixa, Inc</span>
      </div>
      <p class="tagline">Consulting, Licensing and Branding Specialists</p>
    </div>
    <div class="contact-block">
      <span class="person-name">Dilan Vesterby</span>
      <span class="divider"></span>
      <ul class="contact-list">
        <li>
          <svg viewBox="0 0 16 16" aria-hidden="true"><path d="M3.6 1.5l2.3 2.3-1.4 2a9 9 0 0 0 5.7 5.7l2-1.4 2.3 2.3-1.7 2.1C7.6 16 0 8.4 1.5 3.2z"/></svg>
          206-555-0147
        </li>
        <li>
          <svg viewBox="0 0 16 16" aria-hidden="true"><path d="M8 0a5.5 5.5 0 0 0-5.5 5.5C2.5 9.6 8 16 8 16s5.5-6.4 5.5-10.5A5.5 5.5 0 0 0 8 0zm0 8a2.5 2.5 0 1 1 0-5 2.5 2.5 0 0 1 0 5z"/></svg>
          Seattle, WA
        </li>
        <li>
          <svg viewBox="0 0 16 16" aria-hidden="true"><path d="M1 3h14v1.2L8 9 1 4.2zM1 5.8l7 4.8 7-4.8V13H1z"/></svg>
          Dilan@pulvanixa.com
        </li>
      </ul>
    </div>
  </section>
</main>
</body>
</html>
```